Scholar Pathways - educational consulting

I am beginning an educational consultation business - focusing on Tribal (Native American Indian) Communities, but will work with anyone. I have work experience in K-12 and Higher Education. Special Education - transition from school to work. Advising and facilitating with academic skills in higher education. I have a BS - Special Education, Masters - Educational Administration and working on a PhD in Higher Education. Also completing QMR approved certification as an Academic Life Coach

Target Market(s)

K12 college bound students and parents, Trbal Crossings college bound students and families, special education college bound students and parents

Industry/Entity Type

Business

Contact Information for Business Card

Dorena Lyle Fassett. PO Box 417, Cushing, OK 74023. (918) 555-0283. dorena@scholarpathwaysmail.net

Requirements
Must have
• Scholar Pathways is the name of the business - Trbal Crossings is a focus area
Nice to have
• Tourquoise would be nice. I do not have a logo yet

```html
<!DOCTYPE html>
<html lang="en">
<head>
<meta charset="UTF-8">
<title>Scholar Pathways – Business Card</title>
<link href="https://fonts.googleapis.com/css2?family=Open+Sans:ital,wght@0,400;0,600;0,700;1,400&display=swap" rel="stylesheet">
<style>
  :root {
    --teal: #48d1a2;
    --white: #ffffff;
  }
  html, body {
    margin: 0;
    padding: 0;
    overflow: hidden;
    background: var(--white);
  }
  .card {
    position: relative;
    width: 1200px;
    height: 702px;
    background: var(--white);
    font-family: "Open Sans", Arial, sans-serif;
    color: var(--teal);
    overflow: hidden;
  }
  .brand {
    position: absolute;
    left: 71px;
    top: 227px;
    width: 472px;
    height: 149px;
    display: flex;
    flex-direction: column;
    justify-content: center;
    align-items: center;
    font-weight: 700;
    font-size: 62px;
    line-height: 1.05;
    letter-spacing: 3px;
    text-transform: uppercase;
    color: var(--teal);
  }
  .identity {
    position: absolute;
    left: 639px;
    top: 210px;
  }
  .identity__name {
    margin: 0 0 0 11px;
    font-weight: 600;
    font-size: 36px;
    line-height: 1.2;
  }
  .identity__role {
    margin: 0;
    font-style: italic;
    font-weight: 400;
    font-size: 37px;
    line-height: 1.2;
  }
  .contact {
    position: absolute;
    left: 648px;
    top: 348px;
    margin: 0;
    padding: 0;
    list-style: none;
  }
  .contact__item {
    display: flex;
    align-items: center;
    height: 40px;
    margin-bottom: 13px;
    font-size: 31px;
  }
  .contact__icon {
    width: 28px;
    height: 28px;
    margin-right: 11px;
    flex: none;
  }
  .credentials {
    position: absolute;
    left: 0;
    top: 572px;
    width: 1200px;
    height: 130px;
    background: var(--teal);
    color: var(--white);
    display: flex;
    flex-direction: column;
    justify-content: center;
    align-items: center;
    font-weight: 600;
    font-size: 28px;
    line-height: 1.3;
  }
  .credentials p { margin: 0; }
</style>
</head>
<body>
<div class="card">
  <div class="brand">
    <span>Scholar</span>
    <span>Pathways</span>
  </div>

  <div class="identity">
    <p class="identity__name">Dorena Lyle Fassett</p>
    <p class="identity__role">Academic Life Coach</p>
  </div>

  <ul class="contact">
    <li class="contact__item">
      <svg class="contact__icon" viewBox="0 0 28 28" aria-hidden="true">
        <rect width="28" height="28" fill="var(--teal)"/>
        <path d="M6 6h16v4h-6v14h-4V10H6z" fill="var(--white)"/>
      </svg>
      <span>918.555.0283</span>
    </li>
    <li class="contact__item">
      <svg class="contact__icon" viewBox="0 0 28 28" aria-hidden="true">
        <rect width="28" height="28" fill="var(--teal)"/>
        <text x="14" y="23" text-anchor="middle" font-family="Open Sans, Arial, sans-serif" font-weight="700" font-size="26" fill="var(--white)">e</text>
      </svg>
      <span>dorena@scholarpathwaysmail.net</span>
    </li>
  </ul>

  <div class="credentials">
    <p>Bs(Special Education), Masters(Education Administration)</p>
    <p>Phd(Higher Education), QMR Approved Certification</p>
  </div>
</div>
</body>
</html>
```